Business Cards and Logo

KWM - Personal Injury Attorneys is the name of the firm.
We are personal injury lawyers. We want a crisp, modern and impactful design.
Color schemes are white, matte black and light grey OR white, matte black and red OR white, matte black and a nice blue or yellow.
For logo - we don’t want typical logos like scales of justice or a hammer. We want a general design with the KWM letters.
Target Market(s)
People who need attorneys.
Industry/Entity Type
Law Firm
Contact Information for Business Card
Back side: text: Los Angeles - Santa Ana - San Diego - San Francisco
Front side
Name of firm and logo.
Marco Feltrovski
812 W. Colter Ave. 4th Floor
Glendale, CA 91207
(818)555-0172 (c)
(818)555-0194 (o)
Marco@fieldcounselwest.example
Logo Text
KWM
Font styles to use
Other font styles liked:
- Musk - regular. Military - regular. Moonglade. Future. Or similar fonts.
Requirements
Must have
- See above. Nothing else to provide.
- KWM - Personal Injury Attorneys is the name of the firm.
- We are personal injury lawyers. We want a crisp, modern and impactful design.
- Color schemes are white, matte black and light grey OR white, matte black and red OR white, matte black and a nice blue or yellow.
- For logo - we don’t want typical logos like scales of justice or a hammer. We want a general design with the KWM letters.
Nice to have
- See above - nothing else to provide.
Should not have

```html
<!DOCTYPE html>
<html lang="en">
<head>
<meta charset="utf-8">
<title>KWM – Personal Injury Attorneys · Business Cards</title>
<link rel="stylesheet" href="https://fonts.googleapis.com/css2?family=Questrial&display=swap">
<style>
  :root {
    --stage: #2a2a2b;
    --card: #1a1a1b;
    --card-edge: #232324;
    --white: #f4f4f4;
    --red: #e8232a;
    --font: "Questrial", sans-serif;
  }
  * { margin: 0; padding: 0; box-sizing: border-box; }
  html, body {
    width: 1200px; height: 1200px; overflow: hidden;
    background: radial-gradient(circle at 50% 40%, #333334 0%, var(--stage) 70%);
    font-family: var(--font);
    color: var(--white);
  }
  .canvas { position: relative; width: 1200px; height: 1200px; }

  .card {
    position: absolute; left: 180px; width: 840px; height: 480px;
    border-radius: 28px; overflow: hidden;
    background: linear-gradient(160deg, var(--card-edge) 0%, var(--card) 60%);
    box-shadow: 0 18px 40px rgba(0,0,0,.45);
  }
  .card--back { top: 80px; }
  .card--front { top: 640px; }

  .firm-mark { position: absolute; display: flex; align-items: center; gap: 22px; color: var(--white); }
  .firm-mark__name { font-size: 96px; letter-spacing: 2px; line-height: 1; }
  .firm-mark__tagline { font-size: 27px; line-height: 1.02; letter-spacing: 1px; text-transform: uppercase; }

  .card--back .firm-mark { left: 50%; top: 150px; transform: translateX(-50%); }

  .office-list {
    position: absolute; left: 0; right: 0; top: 345px;
    text-align: center; font-size: 19px; letter-spacing: 1px;
  }
  .office-list .dot { color: var(--red); margin: 0 8px; }

  .card--front .firm-mark { right: 40px; top: 60px; }
  .card--front .firm-mark__name { font-size: 112px; }
  .card--front .firm-mark__tagline { font-size: 32px; }

  .card-art { position: absolute; inset: 0; }

  .person-name {
    position: absolute; left: 70px; top: 232px;
    font-size: 30px; letter-spacing: 2px; text-transform: uppercase; color: var(--white);
  }

  .contact-list { position: absolute; left: 40px; top: 315px; list-style: none; }
  .contact-list li { display: flex; align-items: center; gap: 14px; font-size: 24px; letter-spacing: 1px; height: 36px; }
  .contact-list svg { width: 22px; height: 22px; fill: var(--red); flex: none; }

  .office-address {
    position: absolute; right: 60px; top: 355px; text-align: right;
    font-size: 25px; line-height: 1.35; letter-spacing: 1.5px; font-style: normal;
  }
</style>
</head>
<body>
<main class="canvas">

  <section class="card card--back" aria-label="Business card, back">
    <div class="firm-mark">
      <span class="firm-mark__name">KWM</span>
      <span class="firm-mark__tagline">Personal<br>Injury<br>Attorneys</span>
    </div>
    <p class="office-list">Los Angeles<span class="dot">•</span>Santa Ana<span class="dot">•</span>San Diego<span class="dot">•</span>San Francisco</p>
  </section>

  <section class="card card--front" aria-label="Business card, front">
    <svg class="card-art" viewBox="0 0 840 480" aria-hidden="true">
      <polygon points="0,225 430,225 470,285 0,285" fill="var(--red)"/>
      <line x1="470" y1="284" x2="840" y2="284" stroke="var(--red)" stroke-width="2"/>
      <polygon points="640,452 840,452 840,480 610,480" fill="var(--red)"/>
    </svg>

    <div class="firm-mark">
      <span class="firm-mark__name">KWM</span>
      <span class="firm-mark__tagline">Personal<br>Injury<br>Attorneys</span>
    </div>

    <h1 class="person-name">Marco Feltrovski</h1>

    <ul class="contact-list">
      <li>
        <svg viewBox="0 0 24 24"><path d="M7 1h10a2 2 0 0 1 2 2v18a2 2 0 0 1-2 2H7a2 2 0 0 1-2-2V3a2 2 0 0 1 2-2zm0 3v11h10V4zm1 13v1.5h2V17zm3 0v1.5h2V17zm3 0v1.5h2V17zm-6 2.5V21h2v-1.5zm3 0V21h2v-1.5zm3 0V21h2v-1.5z"/></svg>
        <span>(818)555-0172</span>
      </li>
      <li>
        <svg viewBox="0 0 24 24"><path d="M6.6 10.8a15.2 15.2 0 0 0 6.6 6.6l2.2-2.2a1 1 0 0 1 1-.25 11.4 11.4 0 0 0 3.6.57 1 1 0 0 1 1 1V20a1 1 0 0 1-1 1A17 17 0 0 1 3 4a1 1 0 0 1 1-1h3.5a1 1 0 0 1 1 1c0 1.25.2 2.45.57 3.6a1 1 0 0 1-.25 1z"/></svg>
        <span>(818)555-0194</span>
      </li>
      <li>
        <svg viewBox="0 0 24 24"><path d="M2 5h20v14H2zm2 2v.5l8 5.5 8-5.5V7zm0 3v7h16v-7l-8 5.5z"/></svg>
        <span>Marco@fieldcounselwest.example</span>
      </li>
    </ul>

    <address class="office-address">812 W. Colter Ave. 4th Floor<br>Glendale, CA 91207</address>
  </section>

</main>
</body>
</html>
```